Bookkeeping website design

We need a basic site design for wordpress.
We are a bookkeeping business and will need to present a look consistent with the colours and style of the logo.

Target Market(s)

Business owners

Industry/Entity Type

Accounting/Bookkeeping

Coding

Coded - Design and coding required

Number of Pages Required

1 page

```html
<!DOCTYPE html>
<html lang="en">
<head>
<meta charset="utf-8">
<title>Ledgerline Bookkeeping</title>
<link href="https://fonts.googleapis.com/css2?family=Poppins:wght@400;600;700&family=Roboto:wght@400;500;700&display=swap" rel="stylesheet">
<style>
:root{
  --green:#8dc63f;
  --cyan:#00c2f0;
  --blue:#1fa3e0;
  --ink:#222;
  --text:#555;
  --dark:#262626;
  --field:#f1f1f1;
  --line:#c9c9c9;
}
*{box-sizing:border-box;margin:0;padding:0}
html,body{width:1200px;height:3747px;overflow:hidden;background:#fff}
body{position:relative;font-family:"Poppins",sans-serif;color:var(--text)}
.abs{position:absolute}
a{color:inherit;text-decoration:none}

/* header */
.topline{left:0;top:0;width:1200px;height:4px;background:var(--cyan)}
.brand{left:112px;top:38px;display:flex;align-items:center;gap:10px;font:700 24px "Poppins",sans-serif;color:var(--green)}
.brand i{width:26px;height:26px;background:var(--cyan);border-radius:50%;display:block}
.nav{top:50px;font:500 14px "Roboto",sans-serif;color:#333}
.nav.active{color:var(--green)}
.nav.active::after{content:"";display:block;height:3px;background:var(--green);margin-top:6px}
.callicon{left:897px;top:33px;width:50px;height:50px;border-radius:50%;background:var(--green);border:4px solid var(--cyan)}
.calllabel{left:956px;top:38px;font:500 14px "Roboto",sans-serif;color:#222}
.callnum{left:956px;top:56px;font:700 21px "Roboto",sans-serif;color:#222}

/* hero */
.hero-photo{left:0;top:128px;width:1200px;height:700px;background:linear-gradient(100deg,#d8b78a 0%,#c9a57a 25%,#8c8a86 45%,#cfcac3 70%,#e9e6e1 100%)}
.hero-title{left:660px;top:322px;width:470px;font:700 34px/43px "Poppins",sans-serif;color:#fff;text-shadow:0 2px 4px rgba(0,0,0,.45)}
.btn-start{left:660px;top:509px;width:157px;height:47px;border-radius:24px;background:linear-gradient(90deg,var(--cyan),var(--green));color:#fff;font:600 15px/47px "Poppins",sans-serif;text-align:center}
.arrow{left:1121px;width:44px;height:44px;border-radius:50%;background:#111}

/* intro */
.intro-title{left:240px;top:925px;width:720px;text-align:center;font:600 36px/43px "Poppins",sans-serif;color:var(--ink)}
.intro-text{left:200px;top:1068px;width:800px;text-align:center;font:400 17px/26px "Poppins",sans-serif;color:#333}
.intro-text a{color:var(--green)}
.circle{border-radius:50%}
.points{left:601px;top:1138px;width:515px;list-style:none}
.points li{position:relative;padding-left:24px;font:400 14.5px/25.5px "Poppins",sans-serif;color:#666;margin-bottom:26px}
.points li svg{position:absolute;left:0;top:6px}

/* services */
.svc-title{left:112px;top:1880px;font:700 41px "Poppins",sans-serif;color:#fff}
.svc-text{left:112px;top:1945px;width:490px;font:400 15px/22.5px "Poppins",sans-serif;color:#fff}
.svc-text p{margin-bottom:22px}
.svc-list{top:2174px;list-style:none;font:400 15px/22.3px "Poppins",sans-serif;color:#fff}
.svc-list li{display:flex;align-items:center;gap:12px}
.svc-back{left:644px;top:1905px;width:461px;height:411px;background:var(--green);border-radius:40px}
.svc-photo{left:628px;top:1889px;width:460px;height:411px;border-radius:40px;background:linear-gradient(135deg,#e8eef2,#c7d3db 50%,#9aa9b4)}

/* contact */
.contact-title{left:0;top:2604px;width:1200px;text-align:center;font:600 41px "Poppins",sans-serif;color:var(--ink)}
.sub-title{font:600 25px "Poppins",sans-serif;color:#555}
.detail-icon{left:112px;width:46px;height:46px;border-radius:50%;border:2px solid var(--blue);display:flex;align-items:center;justify-content:center}
.detail-label{left:168px;font:700 16px "Roboto",sans-serif;color:#222;letter-spacing:.5px}
.detail-value{left:167px;font:400 17px "Roboto",sans-serif;color:#444}
.field{background:var(--field);border:1px solid var(--line);border-radius:3px;display:flex;align-items:center;gap:10px;padding-left:14px;font:400 12px "Roboto",sans-serif;color:#555}
.field.area{align-items:flex-start;padding-top:16px}
.submit{left:525px;top:3007px;width:134px;height:45px;background:var(--blue);color:#fff;font:700 14px/45px "Roboto",sans-serif;text-align:center}

/* footer */
.footer{left:0;top:3250px;width:1200px;height:497px;background:var(--dark)}
.news-label{left:269px;top:3345px;font:600 21px "Poppins",sans-serif;color:#fff}
.news-box{left:532px;top:3335px;width:357px;height:50px;border:1px solid #bbb;padding:4px}
.news-box span{position:absolute;left:12px;top:16px;font:400 13px "Roboto",sans-serif;color:#888}
.news-btn{position:absolute;right:4px;top:4px;width:116px;height:40px;background:var(--blue);color:#fff;font:500 14px/40px "Roboto",sans-serif;text-align:center}
.rule{left:109px;top:3414px;width:978px;height:1px;background:#444}
.foot-brand{left:102px;top:3512px;display:flex;align-items:center;gap:12px;font:700 34px "Poppins",sans-serif;color:var(--green)}
.foot-brand i{display:block;width:34px;height:34px;background:var(--cyan)}
.col-title{font:600 18px "Poppins",sans-serif;color:#fff}
.col-title::after{content:"";display:block;width:36px;height:2px;background:#fff;margin-top:12px}
.links{list-style:none;font:400 14px/25.8px "Roboto",sans-serif;color:#ddd}
.links li::before{content:"» ";color:#ddd;margin-right:6px}
.fc-icon{width:24px;height:24px;background:var(--blue);display:flex;align-items:center;justify-content:center}
.fc-text{font:400 14px/25px "Roboto",sans-serif;color:#ddd}
.copy{left:0;top:3688px;width:1200px;text-align:center;font:400 14px "Roboto",sans-serif;color:#ddd}
</style>
</head>
<body>

<!-- header -->
<div class="abs topline"></div>
<div class="abs brand"><i></i>Ledgerline</div>
<a class="abs nav active" style="left:451px">HOME</a>
<a class="abs nav" style="left:525px">ABOUT US</a>
<a class="abs nav" style="left:627px">OUR SERVICES</a>
<a class="abs nav" style="left:759px">CONTACT US</a>
<div class="abs callicon">
  <svg width="42" height="42" viewBox="0 0 42 42"><path d="M15 13c1-1 2-1 3 0l2 3c.6 1 .4 2-.4 2.6l-1.2 1c.8 1.8 2.3 3.3 4 4l1-1.2c.6-.8 1.6-1 2.6-.4l3 2c1 .7 1 2 0 3l-1.4 1.4c-4 2-13-7-11-11z" fill="#fff"/></svg>
</div>
<div class="abs calllabel">CONTACT PHONE :</div>
<div class="abs callnum">0400 123 456</div>

<!-- hero -->
<div class="abs hero-photo" role="img" aria-label="Photo of a smiling couple working together on a laptop at home"></div>
<svg class="abs" style="left:0;top:700px" width="1200" height="140" viewBox="0 0 1200 140">
  <path d="M0 50 C250 80 500 50 800 30 C1000 18 1120 20 1200 20 L1200 140 L0 140Z" fill="#fff"/>
  <path d="M0 52 C200 95 420 115 600 85 C800 50 1000 35 1200 28 L1200 32 C1000 45 800 65 600 100 C400 135 200 110 0 80Z" fill="var(--cyan)"/>
  <path d="M0 80 C200 115 400 140 600 104 C800 68 1000 42 1200 32 L1200 36 C1000 50 800 78 600 112 C400 140 180 120 0 86Z" fill="var(--green)"/>
</svg>
<h1 class="abs hero-title">Not getting the balance of work/play you thought you'd have as a small business owner?</h1>
<a class="abs btn-start">GET STARTED</a>
<div class="abs arrow" style="top:390px"><svg width="44" height="44"><path d="M18 25l4-4 4 4" stroke="#fff" stroke-width="1.6" fill="none"/></svg></div>
<div class="abs arrow" style="top:440px"><svg width="44" height="44"><path d="M18 20l4 4 4-4" stroke="#fff" stroke-width="1.6" fill="none"/></svg></div>

<!-- intro -->
<h2 class="abs intro-title">Not getting the balance of work/play you thought you'd have as a small business owner?</h2>
<p class="abs intro-text">Hate doing your BAS? Is it overdue again? Our bookkeepers can help you sort it all out and more! <a>Call us today.</a></p>

<svg class="abs" style="left:300px;top:1150px" width="200" height="400">
  <g fill="#999">
    <circle cx="57" cy="58" r="3"/><circle cx="120" cy="58" r="3"/><circle cx="151" cy="58" r="3"/><circle cx="182" cy="58" r="3"/>
    <circle cx="57" cy="90" r="3"/><circle cx="89" cy="90" r="3"/>
    <circle cx="57" cy="120" r="3"/><circle cx="26" cy="215" r="3"/>
    <circle cx="120" cy="305" r="3"/><circle cx="151" cy="340" r="3"/><circle cx="120" cy="340" r="3"/><circle cx="182" cy="340" r="3"/>
    <circle cx="89" cy="310" r="3"/>
  </g>
</svg>
<div class="abs circle" style="left:127px;top:1153px;width:229px;height:229px;background:linear-gradient(135deg,#19b6e8,#0d86b7)" role="img" aria-label="Photo of colleagues celebrating in an office, tinted blue"></div>
<div class="abs circle" style="left:349px;top:1235px;width:228px;height:228px;background:linear-gradient(135deg,#9fc53a,#4f6a1c)" role="img" aria-label="Photo of two people discussing work at a table, tinted green"></div>
<div class="abs circle" style="left:161px;top:1386px;width:229px;height:229px;background:linear-gradient(135deg,#8a93a8,#3e4964)" role="img" aria-label="Photo of a man and woman reviewing documents at a laptop"></div>
<div class="abs circle" style="left:377px;top:1193px;width:26px;height:26px;background:var(--cyan)"></div>
<div class="abs circle" style="left:116px;top:1399px;width:25px;height:25px;background:var(--green)"></div>
<div class="abs circle" style="left:437px;top:1527px;width:25px;height:25px;background:var(--cyan)"></div>

<ul class="abs points">
  <li><svg width="12" height="12"><circle cx="6" cy="6" r="6" fill="var(--green)"/><path d="M3 6l2 2 4-4" stroke="#fff" stroke-width="1.5" fill="none"/></svg>We are registered BAS service providers who love to help small and medium businesses maintain their financial records and do their BAS. Need an in-house bookkeeper – but not full time?</li>
  <li><svg width="12" height="12"><circle cx="6" cy="6" r="6" fill="var(--green)"/><path d="M3 6l2 2 4-4" stroke="#fff" stroke-width="1.5" fill="none"/></svg>Streamline your bookkeeping with our reliable, seamless and professional service.</li>
  <li><svg width="12" height="12"><circle cx="6" cy="6" r="6" fill="var(--green)"/><path d="M3 6l2 2 4-4" stroke="#fff" stroke-width="1.5" fill="none"/></svg>At Ledgerline Bookkeeping we believe quality costs less at the end of the day. Let's work together to get it right the first time.</li>
  <li><svg width="12" height="12"><circle cx="6" cy="6" r="6" fill="var(--green)"/><path d="M3 6l2 2 4-4" stroke="#fff" stroke-width="1.5" fill="none"/></svg>Are your books out of control? Have you grown too big to manage it all yourself? We help businesses manage their bookkeeping systems regardless of size or industry.</li>
  <li><svg width="12" height="12"><circle cx="6" cy="6" r="6" fill="var(--green)"/><path d="M3 6l2 2 4-4" stroke="#fff" stroke-width="1.5" fill="none"/></svg>We are your bookkeepers North of Perth and are available to come to your office weekly, monthly, quarterly or whenever you need us, you only pay for the time you have booked with us.</li>
</ul>

<!-- services -->
<svg class="abs" style="left:0;top:1680px" width="1200" height="850" viewBox="0 0 1200 850">
  <defs>
    <linearGradient id="svcGrad" x1="0" x2="1" y1="0" y2="0">
      <stop offset="0" stop-color="#94c93d"/><stop offset="0.5" stop-color="#40c9c0"/><stop offset="1" stop-color="#00c8f5"/>
    </linearGradient>
  </defs>
  <path d="M0 96 C250 120 500 60 800 28 C1000 8 1120 12 1200 40 L1200 720 C1000 770 700 780 450 735 C250 700 100 700 0 745Z" fill="url(#svcGrad)"/>
  <path d="M200 110 C500 80 800 10 1100 12 C1150 13 1180 20 1200 30" stroke="#fff" stroke-width="3" fill="none"/>
  <path d="M0 745 C150 700 300 705 450 735 C700 785 1000 770 1200 720 L1200 760 C1000 815 700 830 450 780 C300 750 150 740 0 755Z" fill="var(--green)"/>
  <path d="M420 737 C700 790 1000 770 1200 712" stroke="#fff" stroke-width="3" fill="none"/>
</svg>
<h2 class="abs svc-title">Our Services</h2>
<div class="abs svc-text">
  <p>Getting tired of paperwork? Finding it confusing to balance your books? If you are running a small business, why waste time crunching numbers when you can get it done cost effectively by a bookkeeping professional?</p>
  <p>We offer a complete service package, which means we take care of your accounts, while you take care of your business. We handle all your taxation related needs, covering all aspects of bookkeeping services, including:</p>
</div>
<ul class="abs svc-list" style="left:112px">
  <li><svg width="13" height="13"><circle cx="6.5" cy="6.5" r="6.5" fill="#fff"/><path d="M3.5 6.5l2 2 4-4" stroke="var(--green)" stroke-width="1.6" fill="none"/></svg>GST</li>
  <li><svg width="13" height="13"><circle cx="6.5" cy="6.5" r="6.5" fill="#fff"/><path d="M3.5 6.5l2 2 4-4" stroke="var(--green)" stroke-width="1.6" fill="none"/></svg>BAS</li>
  <li><svg width="13" height="13"><circle cx="6.5" cy="6.5" r="6.5" fill="#fff"/><path d="M3.5 6.5l2 2 4-4" stroke="var(--green)" stroke-width="1.6" fill="none"/></svg>P&amp;L</li>
  <li><svg width="13" height="13"><circle cx="6.5" cy="6.5" r="6.5" fill="#fff"/><path d="M3.5 6.5l2 2 4-4" stroke="var(--green)" stroke-width="1.6" fill="none"/></svg>Balance Sheets</li>
  <li><svg width="13" height="13"><circle cx="6.5" cy="6.5" r="6.5" fill="#fff"/><path d="M3.5 6.5l2 2 4-4" stroke="var(--green)" stroke-width="1.6" fill="none"/></svg>Accounts Payable</li>
  <li><svg width="13" height="13"><circle cx="6.5" cy="6.5" r="6.5" fill="#fff"/><path d="M3.5 6.5l2 2 4-4" stroke="var(--green)" stroke-width="1.6" fill="none"/></svg>Reconciliation</li>
</ul>
<ul class="abs svc-list" style="left:300px">
  <li><svg width="13" height="13"><circle cx="6.5" cy="6.5" r="6.5" fill="#fff"/><path d="M3.5 6.5l2 2 4-4" stroke="var(--green)" stroke-width="1.6" fill="none"/></svg>Payroll</li>
  <li><svg width="13" height="13"><circle cx="6.5" cy="6.5" r="6.5" fill="#fff"/><path d="M3.5 6.5l2 2 4-4" stroke="var(--green)" stroke-width="1.6" fill="none"/></svg>Superannuation</li>
  <li><svg width="13" height="13"><circle cx="6.5" cy="6.5" r="6.5" fill="#fff"/><path d="M3.5 6.5l2 2 4-4" stroke="var(--green)" stroke-width="1.6" fill="none"/></svg>PAYG</li>
  <li><svg width="13" height="13"><circle cx="6.5" cy="6.5" r="6.5" fill="#fff"/><path d="M3.5 6.5l2 2 4-4" stroke="var(--green)" stroke-width="1.6" fill="none"/></svg>Bookwise</li>
  <li><svg width="13" height="13"><circle cx="6.5" cy="6.5" r="6.5" fill="#fff"/><path d="M3.5 6.5l2 2 4-4" stroke="var(--green)" stroke-width="1.6" fill="none"/></svg>Consultancy</li>
  <li><svg width="13" height="13"><circle cx="6.5" cy="6.5" r="6.5" fill="#fff"/><path d="M3.5 6.5l2 2 4-4" stroke="var(--green)" stroke-width="1.6" fill="none"/></svg>Training</li>
</ul>
<div class="abs svc-back"></div>
<div class="abs svc-photo" role="img" aria-label="Photo of a desk with keyboard, calculator, glasses and a hand writing notes"></div>

<!-- contact -->
<h2 class="abs contact-title">Contact us</h2>
<h3 class="abs sub-title" style="left:112px;top:2694px">Contact Details</h3>
<div class="abs detail-icon" style="top:2753px"><svg width="16" height="20"><path d="M8 1a6 6 0 0 1 6 6c0 5-6 12-6 12S2 12 2 7a6 6 0 0 1 6-6z" fill="var(--blue)"/><circle cx="8" cy="7" r="2.3" fill="#fff"/></svg></div>
<div class="abs detail-label" style="top:2752px">ADDRESS</div>
<div class="abs detail-value" style="top:2776px">Banksia Point, Western Australia 6040</div>
<div class="abs detail-icon" style="top:2847px"><svg width="16" height="20"><path d="M8 1a6 6 0 0 1 6 6c0 5-6 12-6 12S2 12 2 7a6 6 0 0 1 6-6z" fill="var(--blue)"/><circle cx="8" cy="7" r="2.3" fill="#fff"/></svg></div>
<div class="abs detail-label" style="top:2846px">PHONE</div>
<div class="abs detail-value" style="top:2870px;font-weight:500">0400 123 456</div>
<div class="abs detail-icon" style="top:2941px"><svg width="20" height="14"><rect x="1" y="1" width="18" height="12" rx="1" fill="var(--blue)"/><path d="M1.5 2l8.5 6 8.5-6" stroke="#fff" stroke-width="1.3" fill="none"/></svg></div>
<div class="abs detail-label" style="top:2939px">E MAIL</div>
<div class="abs detail-value" style="top:2963px;font-size:16px">hello@ledgerlinebooks.com.au</div>

<h3 class="abs sub-title" style="left:525px;top:2686px">Get In Touch</h3>
<div class="abs field" style="left:525px;top:2736px;width:276px;height:45px"><svg width="12" height="13"><circle cx="6" cy="4" r="3.3" fill="var(--blue)"/><path d="M0 13c0-4 3-5.5 6-5.5s6 1.5 6 5.5z" fill="var(--blue)"/></svg>FIRST NAME</div>
<div class="abs field" style="left:812px;top:2736px;width:276px;height:45px"><svg width="12" height="13"><circle cx="6" cy="4" r="3.3" fill="var(--blue)"/><path d="M0 13c0-4 3-5.5 6-5.5s6 1.5 6 5.5z" fill="var(--blue)"/></svg>LAST NAME</div>
<div class="abs field" style="left:525px;top:2797px;width:276px;height:46px"><svg width="16" height="11"><rect width="16" height="11" rx="1" fill="var(--blue)"/><path d="M.5 1l7.5 5 7.5-5" stroke="#fff" stroke-width="1.2" fill="none"/></svg>EMAIL</div>
<div class="abs field" style="left:812px;top:2797px;width:276px;height:46px"><svg width="13" height="13" viewBox="12 12 18 18"><path d="M15 13c1-1 2-1 3 0l2 3c.6 1 .4 2-.4 2.6l-1.2 1c.8 1.8 2.3 3.3 4 4l1-1.2c.6-.8 1.6-1 2.6-.4l3 2c1 .7 1 2 0 3l-1.4 1.4c-4 2-13-7-11-11z" fill="var(--blue)"/></svg>PHONE</div>
<div class="abs field area" style="left:525px;top:2860px;width:563px;height:130px"><svg width="12" height="12"><path d="M1 1l10 10" stroke="var(--blue)" stroke-width="2"/></svg>MESSAGE</div>
<a class="abs submit">SUBMIT</a>

<!-- footer -->
<svg class="abs" style="left:0;top:3150px" width="1200" height="110" viewBox="0 0 1200 110">
  <path d="M0 95 C300 110 600 60 900 30 C1050 16 1150 14 1200 16 L1200 110 L0 110Z" fill="var(--dark)"/>
  <path d="M250 90 C550 75 800 25 1050 12 C1120 8 1170 8 1200 10 L1200 14 C1100 12 1000 20 900 30 C650 55 450 85 250 92Z" fill="var(--cyan)"/>
  <path d="M500 70 C750 40 950 12 1200 4 L1200 9 C1000 12 800 35 500 72Z" fill="var(--green)"/>
</svg>
<div class="abs footer"></div>
<div class="abs news-label">Subscribe Newsletter</div>
<div class="abs news-box"><span>Email Address</span><a class="news-btn">SUBSCRIBE</a></div>
<div class="abs rule"></div>
<div class="abs foot-brand"><i></i>Ledgerline</div>

<div class="abs col-title" style="left:467px;top:3450px">Information</div>
<ul class="abs links" style="left:467px;top:3502px">
  <li>Privacy policy</li><li>Terms &amp; condition</li><li>Support</li><li>Cookies</li><li>Services</li>
</ul>
<div class="abs col-title" style="left:689px;top:3450px">Quick Links</div>
<ul class="abs links" style="left:689px;top:3502px">
  <li>Home</li><li>About Us</li><li>Services</li><li>Rates</li><li>Contact us</li>
</ul>
<div class="abs col-title" style="left:883px;top:3450px">Contact us</div>
<div class="abs fc-icon" style="left:883px;top:3495px"><svg width="10" height="13"><path d="M5 .5a4 4 0 0 1 4 4c0 3.5-4 8-4 8s-4-4.5-4-8a4 4 0 0 1 4-4z" fill="#fff"/></svg></div>
<div class="abs fc-text" style="left:919px;top:3490px">Banksia Point,<br>Western Australia 6040</div>
<div class="abs fc-icon" style="left:883px;top:3556px"><svg width="12" height="12" viewBox="12 12 18 18"><path d="M15 13c1-1 2-1 3 0l2 3c.6 1 .4 2-.4 2.6l-1.2 1c.8 1.8 2.3 3.3 4 4l1-1.2c.6-.8 1.6-1 2.6-.4l3 2c1 .7 1 2 0 3l-1.4 1.4c-4 2-13-7-11-11z" fill="#fff"/></svg></div>
<div class="abs fc-text" style="left:919px;top:3557px">0400 123 456</div>
<div class="abs fc-icon" style="left:883px;top:3603px"><svg width="13" height="9"><rect width="13" height="9" fill="#fff"/><path d="M.5 .5l6 4 6-4" stroke="var(--blue)" stroke-width="1" fill="none"/></svg></div>
<div class="abs fc-text" style="left:919px;top:3603px">hello@ledgerlinebooks.com.au</div>
<div class="abs copy">© Copyright @2021 Company name | All Rights Reserved</div>

</body>
</html>
```